Redesign of Engineering firm website

I want a redesign of the torvelpower.com website with the below in mind:

1- the client has a 3 main sectors: Renewable Energy, Process Automation and General Engineering.
2- Home page should show the 3 sectors
3- the other standard pages should be home, About, Clients, Projects, Training, Career, and Contact
4- The theme should be wordpress.
5- Responsive layout that works with all devices
6- One page layout is preferable for the home page.
7- it should be original and is not copied from other templates.
Updates

Reason: As requested from so many designers... the deadline is extended. Thank you

Target Market(s)

Engineers and professional

Industry/Entity Type

Solar Energy

Font styles to use
Serif
Sans Serif

Colors
3277b5
0355a3
0493ce

Requirements
Must have
• pictures that represent the three sectors

```html
<!DOCTYPE html>
<html lang="en">
<head>
<meta charset="utf-8">
<title>Torvel Power – Home</title>
<link href="https://fonts.googleapis.com/css2?family=Arimo:wght@400;700&family=Roboto:wght@400;500&display=swap" rel="stylesheet">
<style>
:root{
  --blue-dark:#0355a3;
  --blue-mid:#3277b5;
  --blue-light:#0493ce;
  --text:#333333;
  --muted:#666666;
  --panel:#f0f0f0;
  --white:#ffffff;
  --dark:#333333;
}
*{margin:0;padding:0;box-sizing:border-box}
html,body{width:1200px;height:1200px;overflow:hidden;background:var(--white);font-family:"Arimo",Arial,sans-serif;color:var(--text)}
.page{position:relative;width:1200px;height:1200px;overflow:hidden}

.topbar{position:absolute;left:0;top:0;width:1200px;height:36px;background:var(--blue-dark);color:var(--white);font-size:11px}
.topbar .contact{position:absolute;left:110px;top:11px}
.topbar .social{position:absolute;right:117px;top:10px;display:flex;gap:18px}
.topbar .social span{width:14px;height:14px;border-radius:50%;border:2px solid var(--white);display:block}

.header{position:absolute;top:36px;left:0;width:1200px;height:82px;background:var(--white)}
.brand{position:absolute;left:122px;top:24px;display:flex;align-items:center;gap:8px;font-family:"Roboto",sans-serif;font-weight:500;font-size:28px;color:var(--blue-light);letter-spacing:.5px}
.brand .dot{width:12px;height:12px;border-radius:50%;background:var(--blue-light)}
.nav{position:absolute;left:470px;top:0;width:612px;height:82px;display:flex;justify-content:space-between;padding-right:34px;font-family:"Roboto",sans-serif;font-size:13px}
.nav a{color:var(--text);text-decoration:none;padding-top:34px;border-top:2px solid transparent;white-space:nowrap}
.nav a.active{color:var(--blue-mid);border-top-color:var(--blue-mid)}
.nav .search{position:absolute;right:0;top:37px}

.hero{position:absolute;top:118px;left:0;width:1191px;height:506px;background:linear-gradient(180deg,#4f8fd0 0%,#a9cdef 45%,#e9f2fb 62%,#7fc24a 82%,#2c6fa5 100%)}
.hero h1{position:absolute;left:110px;top:189px;width:473px;height:78px;background:rgba(70,70,75,.72);color:var(--white);font-family:"Arimo",sans-serif;font-weight:400;font-size:52px;line-height:78px;padding-left:14px}
.hero .btn{position:absolute;left:111px;top:300px;width:116px;height:38px;background:var(--blue-dark);color:var(--white);font-family:"Roboto",sans-serif;font-size:12px;text-align:center;line-height:38px}
.to-top{position:absolute;left:1137px;width:42px;background:var(--dark);display:flex;align-items:center;justify-content:center}

.sectors{position:absolute;top:690px;left:104px;width:999px;display:flex}
.sector{width:333px;text-align:center}
.sector .photo{width:70px;height:70px;border:1.5px solid var(--blue-dark);border-radius:50%;margin:0 auto}
.photo-renewable{background:linear-gradient(180deg,#5d9ad6 0%,#b9d8f2 55%,#7fc24a 100%)}
.photo-automation{background:linear-gradient(160deg,#c9d3dc 0%,#7f94a8 55%,#3e5873 100%)}
.photo-engineering{background:linear-gradient(180deg,#e7c88a 0%,#a8a9ab 55%,#56626e 100%)}
.sector h3{font-family:"Roboto",sans-serif;font-weight:400;font-size:16px;color:var(--blue-dark);margin-top:16px}
.sector p{font-size:12.5px;line-height:18.5px;color:var(--muted);margin:14px auto 0;width:310px}
.sector p b{color:#555}

.about{position:absolute;top:1006px;left:0;width:1191px;height:194px;background:var(--panel)}
.about h2{position:absolute;left:118px;top:58px;font-weight:400;font-size:38px;color:var(--text)}
.about p{position:absolute;left:118px;top:130px;width:475px;font-size:12.5px;line-height:18.5px;color:var(--muted)}
.about .visual{position:absolute;left:722px;top:54px;width:268px;height:150px;border-radius:40px 40px 0 0;background:linear-gradient(160deg,#c6dbee,#6aa6d6 60%,#2b88c8)}
</style>
</head>
<body>
<div class="page">
  <div class="topbar">
    <div class="contact">Call Us Today! +966135550147 &nbsp;|&nbsp; info@torvelpower.com</div>
    <div class="social"><span></span><span></span><span></span><span></span></div>
  </div>

  <header class="header">
    <div class="brand"><span class="dot"></span>Torvel Power</div>
    <nav class="nav">
      <a class="active">Home</a><a>About Us</a><a>Clients</a><a>Projects</a><a>Training</a><a>Career</a><a>Contact Us</a>
      <svg class="search" width="12" height="12" viewBox="0 0 12 12"><circle cx="5" cy="5" r="3.8" fill="none" stroke="#333" stroke-width="1.8"/><line x1="8" y1="8" x2="11" y2="11" stroke="#333" stroke-width="2"/></svg>
    </nav>
  </header>

  <section class="hero" role="img" aria-label="Wind turbines and solar panels on a green hill under a blue sky">
    <h1>Renewable Energy</h1>
    <div class="btn">READ MORE</div>
  </section>
  <div class="to-top" style="top:582px;height:29px"><svg width="12" height="8" viewBox="0 0 12 8"><path d="M1 7L6 2L11 7" fill="none" stroke="#fff" stroke-width="2"/></svg></div>

  <section class="sectors">
    <div class="sector">
      <div class="photo photo-renewable" role="img" aria-label="Photo of solar panels and wind turbines"></div>
      <h3>Renewable Energy</h3>
      <p><b>Lorem Ipsum</b> is simply dummy text of the printing and typesetting industry. Lorem Ipsum has been the industry's standard dummy text ever since the 1500s, when an unknown printer took a galley of type and scrambled it to make a type specimen book.</p>
    </div>
    <div class="sector">
      <div class="photo photo-automation" role="img" aria-label="Photo of an automated control room and process line"></div>
      <h3>Process Automation</h3>
      <p><b>Lorem Ipsum</b> is simply dummy text of the printing and typesetting industry. Lorem Ipsum has been the industry's standard dummy text ever since the 1500s, when an unknown printer took a galley of type and scrambled it to make a type specimen book</p>
    </div>
    <div class="sector">
      <div class="photo photo-engineering" role="img" aria-label="Photo of an engineering site with steel structures"></div>
      <h3>General Engineering</h3>
      <p><b>Lorem Ipsum</b> is simply dummy text of the printing and typesetting industry. Lorem Ipsum has been the industry's standard dummy text ever since the 1500s, when an unknown printer took a galley of type and scrambled it to make a type specimen book</p>
    </div>
  </section>

  <section class="about">
    <h2>About Us</h2>
    <p>We are the solar experts in the solar kingdom. The KSA (Saudi Arabia) solar market is a promising market with huge potential. The plan is to build 41,000 MW of solar in the coming 20 years, as announced by N.E.R.A. (National Energy Resources Authority). We provide complete solar systems across the region</p>
    <div class="visual" role="img" aria-label="Recycling arrows filled with wind turbine, solar panel and water imagery"></div>
  </section>
  <div class="to-top" style="top:988px;height:31px"><svg width="12" height="8" viewBox="0 0 12 8"><path d="M1 7L6 2L11 7" fill="none" stroke="#fff" stroke-width="2"/></svg></div>
</div>
</body>
</html>
```